Scotch Whisky Label design

To create a unique Label for private bottling of rare single malt island whisky. Distilled in 1997 the whisky is 23 years and from the Island Of Arran. Design should encompass front label+ technical information (volume /drink waring /Alcohol % etc - all to be supplied) for the back lablel. Label should be CMYK only for digital printing. Label can include the island name but only as secondary information as thre brand Corrvale Malt Whisky is protected. Size of front label = approx 80mm x 120mm(portrait).

Design should be simple and effective, but to show quality and uniqueness of whisky

reference web link for ideas

https://www.dramlotbidhouse.example/auctions/148_the-107th-auction/?page=12&area=

images show other similar items

images also show options for bottle style

Target Market(s)

Private buyers of rare whisky

Requirements
Must have
• Age of whisky (23 years)
• Single Island Corrvale Malt (in sub text)
Nice to have
• Traditonal illustration, reference of island geography
Should not have
• metalics,

```html
<!DOCTYPE html>
<html lang="en">
<head>
<meta charset="utf-8">
<title>Single Malt Island Whisky – 23 Year Label</title>
<link rel="stylesheet" href="https://fonts.googleapis.com/css2?family=Oranienbaum&family=Libre+Baskerville:wght@400;700&family=Oswald:wght@400;500&display=swap">
<style>
  :root {
    --page: #f5f5f7;
    --paper: #e6dcaa;
    --paper-edge: #d9cd96;
    --ink: #4e1d0f;
    --ink-soft: #6b3a22;
    --badge: #4a1a10;
    --badge-text: #f1ecdf;
    --scene-light: #d6c596;
    --scene-dark: #9c8456;
  }
  html, body {
    margin: 0;
    width: 1200px;
    height: 1200px;
    overflow: hidden;
    background: var(--page);
  }
  .canvas {
    position: relative;
    width: 1200px;
    height: 1200px;
  }
  .label {
    position: absolute;
    left: 314px;
    top: 80px;
    width: 572px;
    height: 1040px;
    background: linear-gradient(90deg, var(--paper-edge), var(--paper) 12%, var(--paper) 88%, var(--paper-edge));
    color: var(--ink);
  }
  .label__frame {
    position: absolute;
    inset: 21px;
    border: 2px solid var(--ink);
  }
  .rule {
    position: absolute;
    height: 9px;
    border-top: 3px solid var(--ink);
    border-bottom: 1px solid var(--ink);
  }
  .rule--top-left { left: 52px; width: 194px; top: 86px; }
  .rule--top-right { left: 340px; width: 191px; top: 86px; }
  .rule--bottom-left { left: 32px; width: 204px; top: 979px; }
  .rule--bottom-right { left: 346px; width: 194px; top: 979px; }
  .centered {
    position: absolute;
    left: 0;
    right: 0;
    text-align: center;
    margin: 0;
  }
  .label__category {
    top: 145px;
    font-family: "Oranienbaum", serif;
    font-size: 46px;
    letter-spacing: 2px;
    font-weight: 400;
    color: var(--ink-soft);
  }
  .label__title {
    top: 204px;
    font-family: "Libre Baskerville", serif;
    font-weight: 700;
    font-size: 56px;
    letter-spacing: 1px;
  }
  .age-mark {
    position: absolute;
    left: 86px;
    top: 300px;
    width: 400px;
    height: 200px;
  }
  .label__origin {
    top: 505px;
    font-family: "Libre Baskerville", serif;
    font-size: 21px;
  }
  .label__scene {
    position: absolute;
    left: 93px;
    top: 559px;
    width: 398px;
    height: 270px;
    background: linear-gradient(180deg, var(--scene-light) 0%, #c8b480 45%, var(--scene-dark) 100%);
  }
  .label__provenance {
    top: 855px;
    font-family: "Libre Baskerville", serif;
    font-size: 13px;
    letter-spacing: 1px;
  }
  .label__spec {
    position: absolute;
    top: 930px;
    font-family: "Oswald", sans-serif;
    font-weight: 500;
    font-size: 26px;
    margin: 0;
  }
  .label__spec--volume { left: 80px; }
  .label__spec--strength { right: 72px; }
</style>
</head>
<body>
<main class="canvas">
  <section class="label">
    <div class="label__frame"></div>
    <div class="rule rule--top-left"></div>
    <div class="rule rule--top-right"></div>

    <p class="centered label__category">SINGLE MALT ISLAND</p>
    <h1 class="centered label__title">WHISKY</h1>

    <svg class="age-mark" viewBox="0 0 400 200" aria-label="Distilled 1997, aged 23 years">
      <defs>
        <path id="distilled-arc" d="M128 92 A75 75 0 0 1 272 92"/>
      </defs>
      <text font-family="Oranienbaum, serif" font-size="30" fill="var(--ink)" letter-spacing="2">
        <textPath href="#distilled-arc" startOffset="50%" text-anchor="middle">DISTILLED</textPath>
      </text>
      <text x="104" y="72" font-family="Oranienbaum, serif" font-size="36" fill="var(--ink)" text-anchor="middle">19</text>
      <text x="296" y="72" font-family="Oranienbaum, serif" font-size="36" fill="var(--ink)" text-anchor="middle">97</text>
      <g fill="none" stroke="var(--ink)" stroke-width="2.5">
        <path d="M22 102 L140 102 M22 160 L140 160 M22 102 L8 131 L22 160"/>
        <path d="M378 102 L260 102 M378 160 L260 160 M378 102 L392 131 L378 160"/>
      </g>
      <text x="80" y="143" font-family="Oswald, sans-serif" font-size="36" fill="var(--ink)" text-anchor="middle">AGE</text>
      <text x="320" y="143" font-family="Oswald, sans-serif" font-size="36" fill="var(--ink)" text-anchor="middle">YEAR</text>
      <circle cx="200" cy="131" r="66" fill="none" stroke="var(--ink)" stroke-width="2"/>
      <circle cx="200" cy="131" r="58" fill="var(--badge)"/>
      <text x="200" y="155" font-family="Oswald, sans-serif" font-weight="500" font-size="64" fill="var(--badge-text)" text-anchor="middle">23</text>
    </svg>

    <p class="centered label__origin">SINGLE ISLAND CORRVALE MALT</p>

    <div class="label__scene" role="img" aria-label="Sepia engraving of a coastal castle on the shore with a beached sailing boat and hills beyond"></div>

    <p class="centered label__provenance">DISTILLED AND BOTTLED IN SCOTLAND</p>

    <p class="label__spec label__spec--volume">70 CL</p>
    <p class="label__spec label__spec--strength">45%ABV</p>

    <div class="rule rule--bottom-left"></div>
    <div class="rule rule--bottom-right"></div>
  </section>
</main>
</body>
</html>
```